Please use logo from the attachment. We are servicing cable and network electronics. Please read more about our company if you want to get more inspiration

Company Name: Copper Lantern Solutions

https://www.copperlantern-example.com/main/

```html
<!DOCTYPE html>
<html lang="en">
<head>
<meta charset="utf-8">
<title>Copper Lantern Solutions – Business Card</title>
<link href="https://fonts.googleapis.com/css2?family=Montserrat:wght@400;500;700&display=swap" rel="stylesheet">
<style>
  :root {
    --backdrop: #e9e9e9;
    --card-light: #dcdcdc;
    --card-mid: #c4c4c4;
    --card-dark: #b3b3b3;
    --ink: #1e1e1e;
    --brand-blue: #2f8fd8;
    --rule-blue: #3a9be0;
  }
  html, body {
    margin: 0;
    width: 1200px;
    height: 800px;
    overflow: hidden;
    background: var(--backdrop);
    font-family: "Montserrat", sans-serif;
  }
  .canvas {
    position: relative;
    width: 1200px;
    height: 800px;
  }
  .card {
    position: absolute;
    top: 283px;
    width: 430px;
    height: 237px;
    background: linear-gradient(135deg, var(--card-light) 0%, var(--card-mid) 55%, var(--card-dark) 100%);
    box-shadow: 0 10px 22px rgba(0,0,0,0.22);
  }
  .card--front { left: 111px; }
  .card--back  { left: 637px; }

  .brand-name {
    color: var(--brand-blue);
    font-weight: 700;
    white-space: nowrap;
  }
  .card--front .brand-name {
    position: absolute;
    left: 28px;
    top: 100px;
    font-size: 11px;
  }
  .brand-rule {
    position: absolute;
    left: 200px;
    right: 0;
    top: 107px;
    height: 2px;
    background: var(--rule-blue);
  }
  .contact-name {
    position: absolute;
    right: 33px;
    top: 72px;
    text-align: right;
    color: var(--ink);
  }
  .contact-name .person {
    font-size: 18px;
    font-weight: 500;
    line-height: 1.1;
  }
  .contact-name .role {
    font-size: 8.5px;
    letter-spacing: 0.5px;
    font-weight: 400;
  }
  .contact-details {
    position: absolute;
    right: 33px;
    top: 114px;
    text-align: right;
    color: var(--ink);
    font-size: 10.5px;
    line-height: 14.5px;
  }
  .contact-details .small { font-size: 9.5px; line-height: 12px; }

  .back-pattern {
    position: absolute;
    inset: 22px 40px;
    background: radial-gradient(ellipse at center, rgba(150,150,150,0.18), rgba(150,150,150,0) 70%);
  }
  .card--back .brand-name {
    position: absolute;
    left: 0;
    right: 0;
    top: 102px;
    text-align: center;
    font-size: 24px;
  }
</style>
</head>
<body>
  <main class="canvas">
    <section class="card card--front">
      <div class="brand-name">Copper Lantern Solutions</div>
      <div class="brand-rule"></div>
      <div class="contact-name">
        <div class="person">Marcus Hale</div>
        <div class="role">PRESIDENT</div>
      </div>
      <div class="contact-details">
        <div>418-2290 Vale Rd.</div>
        <div>Harlow Creek Ohio 44120</div>
        <div class="small">+8123-555-014</div>
        <div class="small">info@copperlantern-example.com</div>
        <div>https://www.copperlantern-example.com/main/</div>
      </div>
    </section>

    <section class="card card--back">
      <div class="back-pattern" role="img" aria-label="Faint scattered pattern of small person figures"></div>
      <div class="brand-name">Copper Lantern Solutions</div>
    </section>
  </main>
</body>
</html>
```